New Peanut Butter Brand Needs Product Label

We need a packaging label for a new to market peanut butter product based in the UK. The range of peanut butters will include a range of great flavours. We have been looking at labels to give inspiration and we are liking the less complicated designs that are on a white background (Sample designs are attached).

The company is called 'Breezy Acorn Company' The name could be used in full or shortened to 'Breezy Acorn Co'

The design should be a little fun and cool (not in a childish way), using bright colours and a mixture of fonts would be fine (as long as the text is easy to read)

For the purposes of this design brief text that should be added to the front of the design is

Brand name (As above)
Sea Salt (The flavour of this product)
Chunky (Peanut butter is chunky or smooth right !!)

Allowance should be given for the ingredients panel and standard information used on a food product.

Key phrases that could be used in the design are below

Great source of protein
Heart Healthy
Packed with nutrients

The food container will be a plastic pot and so the labels are slightly curved. I have attached a picture of a similar pot and a label outline an sizing which should be of help.

```html
<!DOCTYPE html>
<html lang="en">
<head>
<meta charset="utf-8">
<title>Breezy Acorn Co – Chunky Sea Salt Label</title>
<link href="https://fonts.googleapis.com/css2?family=Fira+Sans:ital,wght@0,400;0,500;0,700;0,800;1,800&display=swap" rel="stylesheet">
<style>
  :root {
    --backdrop: #d6d7db;
    --label-white: #ffffff;
    --mustard: #d4a22e;
    --nut-brown: #8b5224;
    --peanut-orange: #cd7838;
    --peanut-deep: #c06c30;
    --salt-red: #d9432a;
    --ink: #111111;
  }
  html, body {
    margin: 0;
    padding: 0;
    width: 1200px;
    height: 1000px;
    overflow: hidden;
    background: var(--backdrop);
    font-family: "Fira Sans", Arial, sans-serif;
  }
  .canvas {
    position: relative;
    width: 1200px;
    height: 1000px;
  }
  .label {
    position: absolute;
    left: 340px;
    top: 226px;
    width: 540px;
    height: 569px;
    background: var(--label-white);
    overflow: hidden;
  }
  .texture-band {
    position: absolute;
    left: 0;
    top: 40px;
    width: 182px;
    height: 32px;
    background: var(--mustard);
    color: var(--label-white);
    font-weight: 800;
    font-style: italic;
    font-size: 20px;
    line-height: 32px;
    text-align: right;
    padding-right: 14px;
    box-sizing: border-box;
  }
  .brand-name {
    position: absolute;
    left: 0;
    top: 170px;
    width: 540px;
    margin: 0;
    text-align: center;
    font-weight: 800;
    font-size: 62px;
    line-height: 1;
    color: var(--nut-brown);
    letter-spacing: -0.5px;
  }
  .benefits {
    position: absolute;
    left: 97px;
    top: 357px;
    width: 344px;
    height: 24px;
    border-top: 1.5px solid var(--ink);
    border-bottom: 1.5px solid var(--ink);
    display: flex;
    align-items: center;
    justify-content: center;
    gap: 5px;
    font-weight: 700;
    font-size: 11.5px;
    color: var(--ink);
    white-space: nowrap;
  }
  .benefits .dot {
    width: 6px;
    height: 6px;
    border-radius: 50%;
    background: var(--salt-red);
  }
  .flavour {
    position: absolute;
    left: 0;
    top: 396px;
    width: 540px;
    text-align: center;
    font-size: 21px;
    font-weight: 500;
    color: var(--salt-red);
  }
  .peanut-art {
    position: absolute;
    left: 0;
    bottom: 0;
    width: 540px;
    height: 140px;
    background: linear-gradient(180deg, var(--peanut-orange), var(--peanut-deep));
  }
</style>
</head>
<body>
  <div class="canvas">
    <section class="label">
      <div class="texture-band">Chunky</div>
      <h1 class="brand-name">Breezy Acorn Co</h1>
      <div class="benefits">
        <span>Great source of protein</span><span class="dot"></span>
        <span>Heart healthy</span><span class="dot"></span>
        <span>Packed with nutrients</span>
      </div>
      <div class="flavour">Sea Salt</div>
      <div class="peanut-art" role="img" aria-label="Illustration of a large peanut shell along the bottom edge"></div>
    </section>
  </div>
</body>
</html>
```